International Company needs a Letterhead & Envelope Design

Our Company name is Corvale Brightwick Limited.
We'd like to ask the Designers for the luxurious and sophisticated design. Our logo is very simple and neat with letter logos, so we look forward to more professional and refined designs from Designers.
We look forward to providing you with a great design.
Thanks very much in advance.

```html
<!DOCTYPE html>
<html lang="en">
<head>
<meta charset="utf-8">
<title>Corvale Brightwick Limited – Letterhead &amp; Envelope</title>
<link href="https://fonts.googleapis.com/css2?family=Open+Sans:wght@400;600;700&display=swap" rel="stylesheet">
<style>
  :root {
    --bg: #e3e1dc;
    --paper: #f1f1ea;
    --sheet: #e2e3dd;
    --ink: #2b2c2e;
    --logo: #5c5d60;
    --stripe-dark: #7a7b7e;
    --stripe-light: #b9bab8;
    --band-grey: #a2a3a5;
    --band-mid: #5d5e61;
    --band-dark: #25272a;
    --rule: #b8b8b2;
    --white: #ffffff;
  }
  * { margin: 0; padding: 0; box-sizing: border-box; }
  html, body { width: 1200px; height: 900px; overflow: hidden; }
  body {
    background: var(--bg);
    font-family: "Open Sans", Arial, sans-serif;
    color: var(--ink);
    position: relative;
  }

  /* ---------- Letterhead ---------- */
  .letterhead {
    position: absolute; left: 60px; top: 45px;
    width: 620px; height: 800px;
    background: var(--sheet);
    box-shadow: 0 6px 18px rgba(0,0,0,.18);
    overflow: hidden;
  }
  .letterhead-bands { position: absolute; inset: 0; width: 620px; height: 800px; }
  .letterhead-panel {
    position: absolute; left: 23px; top: 23px; right: 23px;
    height: 756px;
    background: var(--paper);
  }
  .letterhead-header {
    position: absolute; left: 0; right: 0; top: 30px; height: 54px;
    display: flex; align-items: center; gap: 14px;
  }
  .stripes { display: flex; flex-direction: column; gap: 4px; }
  .stripes span { display: block; height: 5px; background: var(--stripe-dark); }
  .stripes span:nth-child(even) { background: var(--stripe-light); }
  .stripes--short { width: 32px; }
  .stripes--long { flex: 1; }
  .brand-name {
    font-weight: 700; font-size: 34px; letter-spacing: .5px;
    color: var(--logo); white-space: nowrap; line-height: 1;
  }

  .letter-body {
    position: absolute; left: 35px; right: 35px; top: 176px;
    font-size: 8.6px; line-height: 13.6px; text-align: justify;
  }
  .salutation { font-size: 13px; line-height: 18px; margin-bottom: 22px; }
  .letter-body p.para { margin-bottom: 33px; }

  .letterhead-footer {
    position: absolute; left: 0; right: 0; bottom: 0; height: 52px;
    font-size: 11.5px;
  }
  .footer-web {
    position: absolute; top: 6px; left: 0; right: 0;
    display: flex; align-items: center; gap: 12px;
    padding: 0 0 0 0; color: #555;
  }
  .footer-web::before, .footer-web::after {
    content: ""; flex: 1; height: 1px; background: var(--rule);
  }
  .footer-contacts {
    position: absolute; bottom: 12px; left: 25px; right: 25px;
    display: flex; justify-content: space-between;
  }

  /* ---------- Envelope ---------- */
  .envelope {
    position: absolute; left: 720px; top: 330px;
    width: 440px; height: 250px;
    background: var(--white);
    box-shadow: 0 6px 18px rgba(0,0,0,.18);
    overflow: hidden;
  }
  .envelope-header {
    position: absolute; left: 0; right: 0; top: 56px;
    display: flex; align-items: center; gap: 8px;
  }
  .envelope-header .stripes span { height: 4px; }
  .envelope-header .stripes { gap: 3px; }
  .envelope-header .stripes--short { width: 16px; }
  .envelope-stripes-top {
    position: absolute; right: 0; top: 16px; width: 250px;
  }
  .envelope-stripes-top span { height: 4px; }
  .envelope-stripes-top.stripes { gap: 3px; }
  .envelope .brand-name { font-size: 22px; }
  .address-lines {
    position: absolute; right: 28px; top: 118px; width: 170px;
    display: flex; flex-direction: column; gap: 26px;
  }
  .address-lines span { display: block; height: 1px; background: #c9c9c3; }
  .envelope-band {
    position: absolute; left: 0; right: 0; bottom: 0; height: 36px;
    background: var(--band-dark); color: #d8d8d8;
    display: flex; align-items: center; justify-content: space-between;
    padding: 0 16px; font-size: 9.5px;
  }
  .envelope-band b { color: var(--white); }
  .envelope-band .divider { color: #777; margin: 0 6px; }
</style>
</head>
<body>

<section class="letterhead" aria-label="Letterhead">
  <svg class="letterhead-bands" viewBox="0 0 620 800" aria-hidden="true">
    <path d="M0 490 Q310 486 620 478 V800 H0 Z" fill="var(--band-grey)"/>
    <path d="M0 577 Q300 560 620 538 V800 H0 Z" fill="var(--band-mid)"/>
    <path d="M0 664 Q320 650 620 628 V800 H0 Z" fill="var(--band-dark)"/>
  </svg>

  <div class="letterhead-panel">
    <header class="letterhead-header">
      <div class="stripes stripes--short"><span></span><span></span><span></span></div>
      <div class="brand-name">Corvale Brightwick</div>
      <div class="stripes stripes--long"><span></span><span></span><span></span><span></span></div>
    </header>

    <div class="letter-body">
      <p class="salutation">Dear Sir,</p>
      <p class="para">Corvale Brightwick Limited is pleased to share this short note with our valued partners. For many years our team has worked across borders to deliver careful service, steady planning and honest advice. We believe that every project deserves attention to detail, clear communication and a calm, reliable approach from the first meeting to the final report we hand over.</p>
      <p class="para">It is our aim to make each exchange simple and useful. The purpose of this letter is to outline the next steps we have agreed, so that both teams can plan their work with confidence and share progress openly.</p>
      <p class="para">Over the coming months our offices in several regions will review current contracts, update shared schedules and confirm delivery dates with each partner. A dedicated manager will be your main point of contact and will send a brief summary every week. Where questions arise, our specialists are ready to meet in person or by call. We also plan to refine our reporting format so that figures, milestones and open tasks are easy to read at a glance. Your feedback on these changes is always welcome and will help shape the way we work together in the future.</p>
      <p class="para">Thank you for your continued trust and support. We value the long relationship between our companies and look forward to building on it with the same care and respect. Should you need any further details about the plans described above, please contact our office by email or telephone and a member of our team will respond promptly. We remain committed to quality, fairness and clear results, and we are confident that the year ahead will bring steady growth for everyone involved in this shared work.</p>
    </div>

    <footer class="letterhead-footer">
      <div class="footer-web"><span>www.<b>corvalebrightwick</b>.com</span></div>
      <div class="footer-contacts">
        <span>Email:-info@<b>corvalebrightwick</b>.com</span>
        <span>Call Us:-<b>0207-555-0148</b></span>
      </div>
    </footer>
  </div>
</section>

<section class="envelope" aria-label="Envelope">
  <div class="stripes envelope-stripes-top"><span></span><span></span><span></span><span></span></div>
  <header class="envelope-header">
    <div class="stripes stripes--short"><span></span><span></span><span></span></div>
    <div class="brand-name">Corvale Brightwick</div>
  </header>
  <div class="address-lines"><span></span><span></span><span></span></div>
  <footer class="envelope-band">
    <span>Email:-info@<b>corvalebrightwick</b>.com<span class="divider">|</span>Call Us:-<b>0207-555-0148</b></span>
    <span>www.<b>corvalebrightwick</b>.com</span>
  </footer>
</section>

</body>
</html>
```